Harbor Scholar Frame

The primary goal would be to develop a new vision for the Harbor Scholar Powerpt. I am attaching an older version called HS, I would like it updated to include our colors and our models with new images that make the presentation more relevant. I am also attaching brochures around the new curriculum. The Links below will give examples to the digital lessons: https://210.quillmora.net/review/content/7c2d4a91-583b-4f7e-b2d6-a4e91c0f5b37/review and https://210.quillmora.net/review/content/9f41b6c3-27da-4e85-81c4-c6d204a8e719/review. the Harbor scholar PWRPT should include some of these images and the color palet from the company brochure which is attached.
Target Market(s)
Education
Look and feel

```html
<!DOCTYPE html>
<html lang="en">
<head>
<meta charset="utf-8">
<title>Harbor Scholar Models</title>
<link rel="stylesheet" href="https://fonts.googleapis.com/css2?family=Open+Sans:ital,wght@0,400;0,600;0,700;1,400;1,600&display=swap">
<style>
:root{
  --page:#d4d4d4;
  --ink:#4a4a4c;
  --dark:#515153;
  --orange:#f7941d;
  --orange-soft:#f5a54a;
  --paper:#ffffff;
  --muted:#8a8a8c;
  --rule:#c9c9cb;
}
*{box-sizing:border-box;margin:0;padding:0}
html,body{width:1200px;height:3596px;overflow:hidden}
body{background:var(--page);font-family:"Open Sans",Arial,sans-serif;color:var(--ink);position:relative}
.slide{position:absolute;width:528px;height:296px;background:var(--paper);overflow:hidden}
.slide.dark{background:var(--dark)}
.fill{position:absolute;inset:0;width:100%;height:100%}
.bgfade{position:absolute;inset:0;background:linear-gradient(120deg,#fafafa 0%,#f1eeec 55%,#f7f7f7 100%)}
.ttl{position:absolute;left:25px;top:20px;font-weight:700;line-height:1.15}
.ttl .pre{display:block;font-weight:400;color:var(--orange);font-size:15px}
.ttl .main{display:block;font-size:17px;color:var(--ink)}
.ttl .sub{display:block;font-weight:400;color:var(--orange-soft);font-size:7px;margin-top:1px}
.foot{position:absolute;left:0;bottom:0;width:100%;height:14px;background:var(--dark);font-size:4.6px;color:#d8d8d8;padding-left:25px;line-height:14px}
.foot .brand{position:absolute;right:14px;top:0;height:14px;width:62px;background:#f2f2f2;color:var(--ink);font-weight:700;font-size:7px;text-align:center;line-height:14px}
.foot .brand::before{content:"";display:inline-block;width:5px;height:5px;background:var(--orange);margin-right:3px;vertical-align:0}
.foot .pg{position:absolute;right:0;top:0;width:14px;height:14px;background:var(--orange);color:#fff;font-size:5px;text-align:center}
.logo{position:absolute;color:#fff;font-weight:600;font-size:17px;letter-spacing:.2px}
.logo::before{content:"";display:inline-block;width:10px;height:10px;background:var(--orange);margin-right:5px;vertical-align:-1px}
.hero-title{position:absolute;color:#fff;font-weight:600;line-height:1.12}
.tagline{position:absolute;color:var(--orange);font-style:italic;font-weight:600;font-size:6px;text-transform:uppercase;letter-spacing:.3px}
/* evolution */
.thumb{position:absolute;width:56px;height:44px;border-radius:5px;box-shadow:0 1px 3px rgba(0,0,0,.3)}
.th1{background:linear-gradient(160deg,#2f5c8c,#1c2f4a)}
.th2{background:linear-gradient(160deg,#dfe4dc,#a9b38f)}
.th3{background:linear-gradient(160deg,#e9dccb,#b59a7a)}
.th4{background:linear-gradient(160deg,#d7e3ef,#8fa8c6)}
.th5{background:linear-gradient(160deg,#c98a6a,#7a4f3a)}
.cap{position:absolute;width:80px;text-align:center;font-size:5.5px;color:var(--muted);line-height:1.3}
.chev{position:absolute;top:177px;height:16px;width:86px;background:var(--dark);color:#fff;font-size:6.5px;font-weight:700;text-align:center;line-height:16px;clip-path:polygon(0 0,90% 0,100% 50%,90% 100%,0 100%,8% 50%)}
.chev.now{background:var(--orange)}
.card{position:absolute;top:118px;width:66px;height:70px;background:#fff;border-radius:6px;box-shadow:0 1px 4px rgba(0,0,0,.25)}
.card .thumb{left:5px;top:5px;box-shadow:none}
.card .yr{position:absolute;bottom:4px;width:100%;text-align:center;font-size:6px;color:var(--ink)}
.card.now .yr{color:var(--orange);font-weight:700}
.gt{position:absolute;top:140px;font-size:14px;color:#9a9a9c}
/* body copy */
.copy{position:absolute;font-size:4.6px;line-height:1.45;color:#6b6b6d;text-align:justify}
.copy p{margin-bottom:3px}
/* loop */
.box{position:absolute;height:28px;background:var(--dark);color:#fff;font-size:5.5px;font-weight:600;text-align:center;border-radius:4px;display:flex;align-items:center;justify-content:center;line-height:1.2}
.sym{position:absolute;font-size:12px;color:#9a9a9c}
/* list */
.blist{position:absolute;left:25px;top:82px;list-style:none;font-size:6.5px;color:var(--ink);width:170px}
.blist li{position:relative;padding-left:22px;margin-bottom:12px;line-height:1.4}
.blist li::before{content:"";position:absolute;left:4px;top:1px;border-left:9px solid var(--ink);border-top:5px solid transparent;border-bottom:5px solid transparent}
/* icon grid */
.ico{position:absolute;width:110px;text-align:center;font-size:5.5px;color:var(--ink);line-height:1.35}
.ico .mark{display:block;margin:0 auto 6px;width:34px;height:34px}
.ico small{display:block;font-size:4.4px;color:var(--muted)}
/* diagram */
.dia{position:absolute;inset:0;width:528px;height:296px}
.lab{font-size:7px;font-weight:600;fill:var(--ink);text-anchor:middle;font-family:"Open Sans",Arial,sans-serif}
.lab.on{fill:var(--orange)}
.arr{stroke:var(--orange);stroke-width:1.1;fill:none;marker-end:url(#ah)}
.arr.dash{stroke-dasharray:3 2}
.q{font-size:26px;font-weight:700;fill:var(--orange);text-anchor:middle;font-family:"Open Sans",Arial,sans-serif}
/* table */
.scan{position:absolute;left:22px;top:84px;width:480px;border-collapse:collapse;font-size:4.6px;color:#6b6b6d}
.scan th{background:var(--dark);color:#fff;font-weight:700;height:30px;font-size:4.8px;padding:0 3px}
.scan td{height:11px;border-bottom:1px solid #e3e3e3;padding:0 4px}
.scan td.c{text-align:center;width:58px}
.scan tr.gap td{height:6px;border-bottom:1px solid #c2c2c2}
.scan td.hs{border-left:1.2px solid var(--orange);border-right:1.2px solid var(--orange)}
.tick{display:inline-block;width:6px;height:6px;border:0.8px solid #8a8a8c;font-size:5px;line-height:5px;text-align:center;color:#555}
</style>
</head>
<body>

<svg width="0" height="0" style="position:absolute" aria-hidden="true">
  <defs>
    <marker id="ah" viewBox="0 0 10 10" refX="9" refY="5" markerWidth="5" markerHeight="5" orient="auto"><path d="M0 0L10 5L0 10z" fill="#f7941d"/></marker>
    <linearGradient id="gGrad" x1="0" y1="0" x2="1" y2="1"><stop offset="0" stop-color="#e9c79a"/><stop offset=".55" stop-color="#d89a4e"/><stop offset="1" stop-color="#8c6a57"/></linearGradient>
    <linearGradient id="gClass" x1="0" y1="0" x2="1" y2="1"><stop offset="0" stop-color="#e6ddd3"/><stop offset=".6" stop-color="#b8a08c"/><stop offset="1" stop-color="#6f5a4c"/></linearGradient>
    <linearGradient id="gTeach" x1="0" y1="0" x2="1" y2="0"><stop offset="0" stop-color="#8a6a55"/><stop offset=".5" stop-color="#c9a98d"/><stop offset="1" stop-color="#2f3d5a"/></linearGradient>
    <linearGradient id="gStud" x1="0" y1="0" x2="1" y2="1"><stop offset="0" stop-color="#a23a3a"/><stop offset=".6" stop-color="#5b2c2c"/><stop offset="1" stop-color="#2b2b2b"/></linearGradient>
    <linearGradient id="gCurr" x1="0" y1="0" x2="1" y2="0"><stop offset="0" stop-color="#e8e8e8"/><stop offset=".6" stop-color="#cfcfcf"/><stop offset="1" stop-color="#3e7a3e"/></linearGradient>
    <symbol id="nodes" viewBox="0 0 528 296">
      <rect x="208" y="102" width="105" height="42" rx="6" fill="url(#gTeach)"/>
      <rect x="56" y="159" width="107" height="42" rx="6" fill="url(#gCurr)"/>
      <rect x="372" y="162" width="112" height="38" rx="6" fill="#ffffff" stroke="#e6e6e6"/>
      <rect x="400" y="165" width="42" height="28" rx="2" fill="#1d4f8f"/>
      <rect x="416" y="193" width="10" height="4" fill="#222"/>
      <rect x="208" y="214" width="105" height="42" rx="6" fill="url(#gStud)"/>
    </symbol>
  </defs>
</svg>

<!-- 1 -->
<section class="slide dark" style="left:61px;top:61px">
  <svg class="fill" viewBox="0 0 528 296" aria-hidden="true">
    <polygon points="190,0 300,0 200,296 130,296" fill="#f7941d"/>
  </svg>
  <svg class="fill" viewBox="0 0 528 296" role="img" aria-label="Photo of a graduate in cap with gold tassel">
    <polygon points="300,0 528,0 528,296 200,296" fill="url(#gGrad)"/>
  </svg>
  <div class="logo" style="left:32px;top:130px">Quorvel</div>
  <div class="hero-title" style="left:32px;top:188px;font-size:20px">Harbor Scholar<br>Models</div>
  <div class="tagline" style="left:32px;top:246px">Connecting learning to careers</div>
</section>

<!-- 2 -->
<section class="slide dark" style="left:611px;top:61px">
  <svg class="fill" viewBox="0 0 528 296" role="img" aria-label="Photo of a graduate in cap with gold tassel">
    <polygon points="282,0 528,0 528,20 282,20" fill="#f7941d"/>
    <polygon points="300,20 528,20 528,296 380,296" fill="url(#gGrad)"/>
    <path d="M254 60 L392 284 L82 284 Z" fill="#f7941d" stroke="#f7941d" stroke-width="14" stroke-linejoin="round"/>
  </svg>
  <div class="logo" style="left:32px;top:34px;font-size:14px">Quorvel</div>
  <div class="hero-title" style="left:32px;top:76px;font-size:25px">Harbor<br>Scholar<br>Models</div>
  <div class="tagline" style="left:32px;top:176px;width:110px;line-height:1.4">Connecting learning to careers</div>
</section>

<!-- 3 -->
<section class="slide" style="left:61px;top:378px">
  <h2 class="ttl"><span class="pre">Evolution of</span><span class="main">Digital Instructional Tools</span></h2>
  <div class="thumb th1" style="left:60px;top:114px" role="img" aria-label="Computer lab"></div>
  <div class="thumb th2" style="left:148px;top:114px" role="img" aria-label="Teacher at whiteboard"></div>
  <div class="thumb th3" style="left:235px;top:114px" role="img" aria-label="Students with laptops"></div>
  <div class="thumb th4" style="left:323px;top:114px" role="img" aria-label="Digital textbook screen"></div>
  <div class="thumb th5" style="left:411px;top:114px" role="img" aria-label="Students using a teaching platform"></div>
  <div class="chev" style="left:45px">1985</div>
  <div class="chev" style="left:133px">2000</div>
  <div class="chev" style="left:221px">2010</div>
  <div class="chev" style="left:309px">2012</div>
  <div class="chev now" style="left:397px">Next Gen.</div>
  <div class="cap" style="left:48px;top:205px">Computer<br>Labs</div>
  <div class="cap" style="left:136px;top:205px">Electronic<br>Whiteboards</div>
  <div class="cap" style="left:223px;top:205px">In-class<br>Computing</div>
  <div class="cap" style="left:311px;top:205px">Print → Digital</div>
  <div class="cap" style="left:399px;top:205px">Harbor Scholar<br>Platforms</div>
  <div class="foot">Quorvel™ Routeway™ 2018 Trademark Quorvel, LLC<span class="brand">Quorvel</span><span class="pg">2</span></div>
</section>

<!-- 4 -->
<section class="slide" style="left:611px;top:378px">
  <h2 class="ttl"><span class="pre">Evolution of</span><span class="main">Digital Instructional Tools</span></h2>
  <div class="card" style="left:55px"><div class="thumb th1" role="img" aria-label="Computer lab"></div><span class="yr">1985</span></div>
  <div class="gt" style="left:124px">›</div>
  <div class="card" style="left:143px"><div class="thumb th2" role="img" aria-label="Teacher at whiteboard"></div><span class="yr">2000</span></div>
  <div class="gt" style="left:213px">›</div>
  <div class="card" style="left:232px"><div class="thumb th3" role="img" aria-label="Students with laptops"></div><span class="yr">2010</span></div>
  <div class="gt" style="left:302px">›</div>
  <div class="card" style="left:321px"><div class="thumb th4" role="img" aria-label="Digital textbook screen"></div><span class="yr">2012</span></div>
  <div class="gt" style="left:391px">›</div>
  <div class="card now" style="left:410px"><div class="thumb th5" role="img" aria-label="Students using a teaching platform"></div><span class="yr">Next Gen.</span></div>
  <div class="cap" style="left:48px;top:208px">Computer<br>Labs</div>
  <div class="cap" style="left:136px;top:208px">Electronic<br>Whiteboards</div>
  <div class="cap" style="left:225px;top:208px">In-class<br>Computing</div>
  <div class="cap" style="left:314px;top:208px">Print →<br>Digital</div>
  <div class="cap" style="left:403px;top:208px">Harbor Scholar<br>Platforms</div>
  <div class="foot">Quorvel™ Routeway™ 2018 Trademark Quorvel, LLC<span class="brand">Quorvel</span><span class="pg">3</span></div>
</section>

<!-- 5 -->
<section class="slide" style="left:61px;top:695px">
  <svg class="fill" viewBox="0 0 528 296" role="img" aria-label="Photo of students working at a classroom table">
    <polygon points="316,0 528,0 528,296 390,296" fill="url(#gClass)"/>
    <polygon points="252,0 316,0 390,296 350,296" fill="#f7941d"/>
    <polygon points="290,0 316,0 390,296 370,296" fill="#515153"/>
  </svg>
  <h2 class="ttl"><span class="pre">Harbor Scholar</span><span class="main">Platforms</span></h2>
  <div class="copy" style="left:25px;top:84px;width:220px">
    <p>The Harbor Scholar Platform combines a full curriculum of guided learning with applied activities, multimedia presentations, practice work and projects. Before class the teacher plans and adapts each lesson; during class the platform supports whole group, small group and individual study, and afterwards reviews progress and grades.</p>
    <p>The platform gives teachers strong tools for planning and managing lessons, tailoring instruction to each learner and delivering timely feedback on every activity. It keeps classrooms organized while respecting the role of schools in preparing students for college and careers.</p>
    <p>At the same time, the platform follows a constructivist approach with open exploration, shared projects and group discussion, helping students connect what they learn today to the work they will do tomorrow.</p>
  </div>
  <div class="foot">Quorvel™ Routeway™ 2018 Trademark Quorvel, LLC</div>
</section>

<!-- 6 -->
<section class="slide" style="left:611px;top:695px">
  <h2 class="ttl" style="top:66px"><span class="pre">Harbor Scholar Platforms</span></h2>
  <div class="copy" style="left:25px;top:96px;width:115px">
    <p>The Harbor Scholar Platform combines a full curriculum of guided learning with applied activities, multimedia presentations, practice work and projects. Before class the teacher plans and adapts each lesson; during class the platform supports whole group, small group and individual study, and afterwards reviews progress and grades.</p>
    <p>The platform gives teachers strong tools for planning and managing lessons, tailoring instruction to each learner and delivering timely feedback on every activity.</p>
  </div>
  <div class="copy" style="left:148px;top:96px;width:115px">
    <p>It keeps classrooms organized while respecting the role of schools in preparing students for college and careers.</p>
    <p>At the same time, the platform follows a constructivist approach with open exploration, shared projects and group discussion, helping students connect what they learn today to the work they will do tomorrow.</p>
  </div>
  <div role="img" aria-label="Book cover on Harbor Scholar platforms" style="position:absolute;left:364px;top:50px;width:128px;height:178px;background:linear-gradient(135deg,#5a5a5c,#2e2e30);box-shadow:3px 3px 6px rgba(0,0,0,.35)"></div>
  <div class="foot">Quorvel™ Routeway™ 2018 Trademark Quorvel, LLC<span class="brand">Quorvel</span><span class="pg">5</span></div>
</section>

<!-- 7 -->
<section class="slide" style="left:61px;top:1012px">
  <div class="bgfade"></div>
  <h2 class="ttl"><span class="pre">Traditional</span><span class="main">LMS Instructional Loop</span></h2>
  <svg class="fill" viewBox="0 0 528 296" aria-hidden="true">
    <path d="M100 98 A58 58 0 0 1 203 108" fill="none" stroke="#f7941d" stroke-width="1.6" marker-end="url(#ah)"/>
    <path d="M203 176 A58 58 0 0 1 100 186" fill="none" stroke="#f7941d" stroke-width="1.6" marker-end="url(#ah)"/>
  </svg>
  <div class="box" style="left:46px;top:128px;width:82px">Content<br>Management</div>
  <div class="sym" style="left:139px;top:132px">›</div>
  <div class="box" style="left:154px;top:128px;width:82px">Assessment</div>
  <div class="sym" style="left:259px;top:132px">›</div>
  <div class="box" style="left:281px;top:128px;width:82px">Grade Book</div>
  <div class="sym" style="left:374px;top:131px">⟷</div>
  <div class="box" style="left:400px;top:128px;width:82px">SIS</div>
  <div class="foot">Quorvel™ Routeway™ 2018 Trademark Quorvel, LLC<span class="brand">Quorvel</span><span class="pg">6</span></div>
</section>

<!-- 8 -->
<section class="slide" style="left:611px;top:1012px">
  <svg class="fill" viewBox="0 0 528 296" role="img" aria-label="Photo of a student presenting at a whiteboard">
    <polygon points="285,0 528,0 528,296 330,296" fill="url(#gClass)"/>
    <polygon points="205,0 260,0 320,296 282,296" fill="#f7941d"/>
    <polygon points="245,0 285,0 330,296 305,296" fill="#515153"/>
  </svg>
  <h2 class="ttl"><span class="pre">Traditional</span><span class="main">LMS</span></h2>
  <ul class="blist">
    <li>Skinnerian Teaching Machines — ILS's</li>
    <li>"Teacher Proof" Technology</li>
    <li>Closed Curriculum</li>
    <li>Fixed Map from Assessment to Curriculum</li>
    <li>Lab or Back of the Room</li>
    <li>One student only</li>
  </ul>
  <div class="foot">Quorvel™ Routeway™ 2018 Trademark Quorvel, LLC</div>
</section>

<!-- 9 -->
<section class="slide" style="left:61px;top:1329px">
  <div class="bgfade"></div>
  <h2 class="ttl"><span class="pre">Traditional</span><span class="main">LMS</span></h2>
  <div class="ico" style="left:26px;top:100px"><svg class="mark" viewBox="0 0 34 34" role="img" aria-label="Teaching machine icon"><rect x="6" y="8" width="22" height="18" rx="2" fill="none" stroke="#4a4a4c" stroke-width="1.5"/><circle cx="17" cy="17" r="5" fill="#f7941d"/></svg>Skinnerian Teaching<br>Machines — ILS's</div>
  <div class="ico" style="left:209px;top:100px"><svg class="mark" viewBox="0 0 34 34" role="img" aria-label="Teacher proof icon"><circle cx="15" cy="12" r="6" fill="none" stroke="#4a4a4c" stroke-width="1.5"/><rect x="8" y="22" width="18" height="8" fill="#f7941d"/></svg>"Teacher Proof"<br>Technology</div>
  <div class="ico" style="left:392px;top:100px"><svg class="mark" viewBox="0 0 34 34" role="img" aria-label="Closed book icon"><circle cx="17" cy="17" r="13" fill="none" stroke="#4a4a4c" stroke-width="1.5"/><rect x="11" y="10" width="12" height="14" fill="#f7941d"/></svg>Closed Curriculum</div>
  <div class="ico" style="left:26px;top:188px"><svg class="mark" viewBox="0 0 34 34" role="img" aria-label="Target icon"><circle cx="17" cy="15" r="10" fill="none" stroke="#4a4a4c" stroke-width="1.5"/><circle cx="17" cy="15" r="4" fill="#f7941d"/></svg>Fixed Map from Assessment<br>to Curriculum</div>
  <div class="ico" style="left:209px;top:188px"><svg class="mark" viewBox="0 0 34 34" role="img" aria-label="Computer lab icon"><rect x="6" y="6" width="22" height="14" fill="none" stroke="#4a4a4c" stroke-width="1.5"/><rect x="6" y="23" width="22" height="6" fill="#f7941d"/></svg>Lab or Back of the<br>Room</div>
  <div class="ico" style="left:392px;top:188px"><svg class="mark" viewBox="0 0 34 34" role="img" aria-label="Single student icon"><circle cx="17" cy="11" r="6" fill="none" stroke="#4a4a4c" stroke-width="1.5"/><path d="M7 30 Q17 16 27 30 Z" fill="#f7941d"/></svg>One Student only</div>
  <div class="foot">Quorvel™ Routeway™ 2018 Trademark Quorvel, LLC<span class="brand">Quorvel</span><span class="pg">8</span></div>
</section>

<!-- 10 -->
<section class="slide" style="left:611px;top:1329px">
  <div class="bgfade"></div>
  <h2 class="ttl"><span class="pre">Where is</span><span class="main">The Locus of Control?</span><span class="sub">Traditional LMS</span></h2>
  <svg class="dia" viewBox="0 0 528 296" role="img" aria-label="Photos of teacher, student, curriculum screen and computer linked to a question mark">
    <use href="#nodes"/>
    <text class="lab" x="260" y="97">Teacher</text><text class="lab" x="110" y="211">Curriculum</text><text class="lab" x="428" y="211">Technology</text><text class="lab" x="260" y="266">Student</text>
    <line class="arr dash" x1="260" y1="147" x2="260" y2="158"/><line class="arr dash" x1="166" y1="180" x2="246" y2="180"/><line class="arr dash" x1="370" y1="180" x2="276" y2="180"/><line class="arr dash" x1="260" y1="212" x2="260" y2="194"/>
    <text class="q" x="261" y="189">?</text>
  </svg>
  <div class="foot">Quorvel™ Routeway™ 2018 Trademark Quorvel, LLC<span class="brand">Quorvel</span><span class="pg">9</span></div>
</section>

<!-- 11 -->
<section class="slide" style="left:61px;top:1646px">
  <div class="bgfade"></div>
  <h2 class="ttl"><span class="main">Teacher-Centered</span><span class="sub">Traditional LMS</span></h2>
  <svg class="dia" viewBox="0 0 528 296" role="img" aria-label="Photos of teacher, student, curriculum screen and computer with arrows pointing to the teacher">
    <use href="#nodes"/>
    <text class="lab on" x="260" y="97">Teacher</text><text class="lab" x="110" y="211">Curriculum</text><text class="lab" x="428" y="211">Technology</text><text class="lab" x="260" y="266">Student</text>
    <line class="arr" x1="166" y1="172" x2="205" y2="140"/><line class="arr" x1="370" y1="170" x2="316" y2="140"/><line class="arr" x1="260" y1="212" x2="260" y2="148"/>
  </svg>
  <div class="foot">Quorvel™ Routeway™ 2018 Trademark Quorvel, LLC<span class="brand">Quorvel</span><span class="pg">10</span></div>
</section>

<!-- 12 -->
<section class="slide" style="left:611px;top:1646px">
  <div class="bgfade"></div>
  <h2 class="ttl"><span class="main">Curriculum-Centered</span><span class="sub">Traditional LMS</span></h2>
  <svg class="dia" viewBox="0 0 528 296" role="img" aria-label="Photos of teacher, student, curriculum screen and computer with arrows pointing to the curriculum">
    <use href="#nodes"/>
    <text class="lab" x="260" y="97">Teacher</text><text class="lab on" x="110" y="211">Curriculum</text><text class="lab" x="428" y="211">Technology</text><text class="lab" x="260" y="266">Student</text>
    <line class="arr" x1="206" y1="130" x2="166" y2="168"/><line class="arr" x1="370" y1="180" x2="167" y2="180"/><line class="arr" x1="206" y1="232" x2="166" y2="193"/>
  </svg>
  <div class="foot">Quorvel™ Routeway™ 2018 Trademark Quorvel, LLC<span class="brand">Quorvel</span><span class="pg">11</span></div>
</section>

<!-- 13 -->
<section class="slide" style="left:61px;top:1963px">
  <div class="bgfade"></div>
  <h2 class="ttl"><span class="main">Student-Centered</span><span class="sub">Traditional LMS</span></h2>
  <svg class="dia" viewBox="0 0 528 296" role="img" aria-label="Photos of teacher, student, curriculum screen and computer with arrows pointing to the student">
    <use href="#nodes"/>
    <text class="lab" x="260" y="97">Teacher</text><text class="lab" x="110" y="211">Curriculum</text><text class="lab" x="428" y="211">Technology</text><text class="lab on" x="260" y="266">Student</text>
    <line class="arr" x1="260" y1="147" x2="260" y2="210"/><line class="arr" x1="166" y1="190" x2="205" y2="224"/><line class="arr" x1="370" y1="190" x2="316" y2="224"/>
  </svg>
  <div class="foot">Quorvel™ Routeway™ 2018 Trademark Quorvel, LLC<span class="brand">Quorvel</span><span class="pg">12</span></div>
</section>

<!-- 14 -->
<section class="slide" style="left:611px;top:1963px">
  <div class="bgfade"></div>
  <h2 class="ttl"><span class="main">Technology-Centered</span><span class="sub">Traditional LMS</span></h2>
  <svg class="dia" viewBox="0 0 528 296" role="img" aria-label="Photos of teacher, student, curriculum screen and computer with arrows pointing to the technology">
    <use href="#nodes"/>
    <text class="lab" x="260" y="97">Teacher</text><text class="lab" x="110" y="211">Curriculum</text><text class="lab on" x="428" y="211">Technology</text><text class="lab" x="260" y="266">Student</text>
    <line class="arr dash" x1="316" y1="132" x2="392" y2="166"/><line class="arr dash" x1="166" y1="180" x2="394" y2="180"/><line class="arr dash" x1="316" y1="230" x2="392" y2="196"/>
  </svg>
  <div class="foot">Quorvel™ Routeway™ 2018 Trademark Quorvel, LLC<span class="brand">Quorvel</span><span class="pg">13</span></div>
</section>

<!-- 15 -->
<section class="slide" style="left:61px;top:2280px">
  <div class="bgfade"></div>
  <h2 class="ttl"><span class="pre">Harbor Scholar Platform</span><span class="main">Instructional Loop</span></h2>
  <div class="ico" style="left:20px;top:96px"><svg class="mark" viewBox="0 0 34 34" role="img" aria-label="Classroom screen icon"><rect x="6" y="6" width="22" height="16" fill="none" stroke="#4a4a4c" stroke-width="1.5"/><path d="M5 30 L17 18 L29 30 Z" fill="#f7941d"/></svg>Designed for<br>Classroom Use<small>Real-Time Classroom<br>Management</small></div>
  <div class="ico" style="left:138px;top:96px"><svg class="mark" viewBox="0 0 34 34" role="img" aria-label="Teacher icon"><circle cx="17" cy="12" r="7" fill="none" stroke="#4a4a4c" stroke-width="1.5"/><path d="M6 30 L17 20 L28 30 Z" fill="#f7941d"/></svg>Teacher-Centric<small>Scaffolds Teachers</small></div>
  <div class="ico" style="left:256px;top:96px"><svg class="mark" viewBox="0 0 34 34" role="img" aria-label="Open curriculum icon"><path d="M6 30 L17 6 L28 30 Z" fill="#f7941d"/><rect x="24" y="6" width="4" height="20" fill="#4a4a4c"/></svg>Open Curriculum—<br>Flexible, Teacher-<br>Modifiable</div>
  <div class="ico" style="left:374px;top:96px"><svg class="mark" viewBox="0 0 34 34" role="img" aria-label="Lesson planning icon"><rect x="8" y="5" width="18" height="22" fill="none" stroke="#4a4a4c" stroke-width="1.5"/><rect x="5" y="24" width="12" height="6" fill="#f7941d"/></svg>Lesson Planning<br>Tools</div>
  <div class="ico" style="left:20px;top:184px"><svg class="mark" viewBox="0 0 34 34" role="img" aria-label="Student group icon"><circle cx="11" cy="12" r="5" fill="none" stroke="#4a4a4c" stroke-width="1.5"/><circle cx="23" cy="12" r="5" fill="none" stroke="#4a4a4c" stroke-width="1.5"/><rect x="6" y="22" width="22" height="8" fill="#f7941d"/></svg>Individual, Group,<br>and Whole Class<br>Curricula</div>
  <div class="ico" style="left:138px;top:184px"><svg class="mark" viewBox="0 0 34 34" role="img" aria-label="Collaboration icon"><circle cx="17" cy="12" r="7" fill="#f7941d"/><rect x="9" y="24" width="16" height="6" fill="none" stroke="#4a4a4c" stroke-width="1.5"/></svg>Collaborative,<br>Project Centered</div>
  <div class="ico" style="left:256px;top:184px"><svg class="mark" viewBox="0 0 34 34" role="img" aria-label="Adaptive assessment icon"><path d="M5 30 L17 6 L29 30 Z" fill="#f7941d"/><circle cx="24" cy="10" r="5" fill="none" stroke="#4a4a4c" stroke-width="1.5"/></svg>Adaptive Assessment<br>Loop for Personalized<br>Instruction</div>
  <div class="foot">Quorvel™ Routeway™ 2018 Trademark Quorvel, LLC<span class="brand">Quorvel</span><span class="pg">14</span></div>
</section>

<!-- 16 -->
<section class="slide" style="left:611px;top:2280px">
  <div class="bgfade"></div>
  <h2 class="ttl"><span class="pre">Where is</span><span class="main">The Locus of Control?</span><span class="sub">HS Platform</span></h2>
  <svg class="dia" viewBox="0 0 528 296" role="img" aria-label="Photos of teacher, student, curriculum screen and computer linked to a question mark">
    <use href="#nodes"/>
    <text class="lab" x="260" y="97">Teacher</text><text class="lab" x="110" y="211">Curriculum</text><text class="lab" x="428" y="211">Technology</text><text class="lab" x="260" y="266">Student</text>
    <line class="arr dash" x1="260" y1="147" x2="260" y2="158"/><line class="arr dash" x1="166" y1="180" x2="246" y2="180"/><line class="arr dash" x1="370" y1="180" x2="276" y2="180"/><line class="arr dash" x1="260" y1="212" x2="260" y2="194"/>
    <text class="q" x="261" y="189">?</text>
  </svg>
  <div class="foot">Quorvel™ Routeway™ 2018 Trademark Quorvel, LLC<span class="brand">Quorvel</span><span class="pg">15</span></div>
</section>

<!-- 17 -->
<section class="slide" style="left:61px;top:2597px">
  <div class="bgfade"></div>
  <h2 class="ttl"><span class="main">Teacher-Centered</span><span class="sub">HS Platform</span></h2>
  <svg class="dia" viewBox="0 0 528 296" role="img" aria-label="Photos of teacher, student, curriculum screen and computer with arrows pointing to the teacher">
    <use href="#nodes"/>
    <text class="lab on" x="260" y="97">Teacher</text><text class="lab" x="110" y="211">Curriculum</text><text class="lab" x="428" y="211">Technology</text><text class="lab" x="260" y="266">Student</text>
    <line class="arr" x1="166" y1="172" x2="205" y2="140"/><line class="arr" x1="370" y1="170" x2="316" y2="140"/><line class="arr" x1="260" y1="212" x2="260" y2="148"/>
  </svg>
  <div class="foot">Quorvel™ Routeway™ 2018 Trademark Quorvel, LLC<span class="brand">Quorvel</span><span class="pg">16</span></div>
</section>

<!-- 18 -->
<section class="slide" style="left:611px;top:2597px">
  <div class="bgfade"></div>
  <h2 class="ttl"><span class="main">Student-Centered</span><span class="sub">HS Platform</span></h2>
  <svg class="dia" viewBox="0 0 528 296" role="img" aria-label="Photos of teacher, student, curriculum screen and computer with arrows pointing to the student">
    <use href="#nodes"/>
    <text class="lab" x="260" y="97">Teacher</text><text class="lab" x="110" y="211">Curriculum</text><text class="lab" x="428" y="211">Technology</text><text class="lab on" x="260" y="266">Student</text>
    <line class="arr dash" x1="260" y1="147" x2="260" y2="210"/><line class="arr dash" x1="166" y1="190" x2="205" y2="224"/><line class="arr dash" x1="370" y1="190" x2="316" y2="224"/>
  </svg>
  <div class="foot">Quorvel™ Routeway™ 2018 Trademark Quorvel, LLC<span class="brand">Quorvel</span><span class="pg">17</span></div>
</section>

<!-- 19 -->
<section class="slide" style="left:61px;top:2914px">
  <h2 class="ttl"><span class="pre">Instructional</span><span class="main">Delivery Scan</span></h2>
  <table class="scan">
    <tr><th style="text-align:center">21st Century School Environment</th><th>Course Platform LMS</th><th>Course Delivery LMS</th><th>Harbor Scholar Platform</th><th>Text book</th><th>e-book</th></tr>
    <tr><td>Interactive Digital Environment</td><td class="c"><span class="tick">✓</span></td><td class="c"></td><td class="c hs"><span class="tick">✓</span></td><td class="c"></td><td class="c"><span class="tick">✓</span></td></tr>
    <tr><td>Virtual Courses</td><td class="c"></td><td class="c"><span class="tick">✓</span></td><td class="c hs"></td><td class="c"></td><td class="c"></td></tr>
    <tr class="gap"><td></td><td></td><td></td><td class="hs"></td><td></td><td></td></tr>
    <tr><td>Teacher Administration Tools</td><td class="c"><span class="tick">✓</span></td><td class="c"><span class="tick">✓</span></td><td class="c hs"><span class="tick">✓</span></td><td class="c"><span class="tick">✓</span></td><td class="c"><span class="tick">✓</span></td></tr>
    <tr><td>Student Administration Tools</td><td class="c"><span class="tick">✓</span></td><td class="c"><span class="tick">✓</span></td><td class="c hs"><span class="tick">✓</span></td><td class="c"></td><td class="c"><span class="tick">✓</span></td></tr>
    <tr class="gap"><td></td><td></td><td></td><td class="hs"></td><td></td><td></td></tr>
    <tr><td>Course Authoring Tools</td><td class="c"><span class="tick">✓</span></td><td class="c"></td><td class="c hs"><span class="tick">✓</span></td><td class="c"></td><td class="c"></td></tr>
    <tr><td>Curriculum Content</td><td class="c"></td><td class="c"><span class="tick">✓</span></td><td class="c hs"><span class="tick">✓</span></td><td class="c"><span class="tick">✓</span></td><td class="c"><span class="tick">✓</span></td></tr>
    <tr><td>Assessment Content</td><td class="c"></td><td class="c"><span class="tick">✓</span></td><td class="c hs"><span class="tick">✓</span></td><td class="c"><span class="tick">✓</span></td><td class="c"><span class="tick">✓</span></td></tr>
    <tr class="gap"><td></td><td></td><td></td><td class="hs"></td><td></td><td></td></tr>
    <tr><td>Classroom Support</td><td class="c"></td><td class="c"></td><td class="c hs"><span class="tick">✓</span></td><td class="c"><span class="tick">✓</span></td><td class="c"></td></tr>
    <tr><td>Pedagogical Support</td><td class="c"></td><td class="c"></td><td class="c hs"><span class="tick">✓</span></td><td class="c"><span class="tick">✓</span></td><td class="c"><span class="tick">✓</span></td></tr>
  </table>
  <div class="foot">Quorvel™ Routeway™ 2018 Trademark Quorvel, LLC<span class="brand">Quorvel</span><span class="pg">18</span></div>
</section>

<!-- 20 -->
<section class="slide dark" style="left:611px;top:2914px">
  <svg class="fill" viewBox="0 0 528 296" role="img" aria-label="Photo of a graduate in cap with gold tassel">
    <polygon points="300,0 528,0 528,296 260,296" fill="url(#gGrad)"/>
    <polygon points="215,0 300,0 270,130 232,130" fill="#f7941d"/>
    <polygon points="0,0 215,0 232,130 0,130" fill="#515153" opacity="0"/>
  </svg>
  <div class="hero-title" style="left:36px;top:200px;font-size:30px">Thank You</div>
</section>

<!-- 21 -->
<section class="slide dark" style="left:61px;top:3231px">
  <svg class="fill" viewBox="0 0 528 296" role="img" aria-label="Photo of a graduate in cap with gold tassel">
    <polygon points="280,30 528,30 528,296 400,296" fill="url(#gGrad)"/>
    <path d="M254 76 L392 284 L130 284 Z" fill="#f7941d" stroke="#f7941d" stroke-width="14" stroke-linejoin="round"/>
  </svg>
  <div class="hero-title" style="left:44px;top:52px;font-size:32px;line-height:1.1">Thank<br>You</div>
</section>

</body>
</html>
```